Plant Based, Environmentally SAFE Chemistry Business requires corporate standards covering all facet

Brightfold Resources is a Canadian based manufacturer and distributor of proprietary chemical formulations made entirely from domestically grown ingredients. These chemicals are non-toxic, non-caustic, contain no VOC's, will readily biodegrade to their natural state within 28 days, are non-corrosive and non-flammable. They carry an enviable 0-0-0-0 hazard rating and are safe for humans, pets and the environment.
We need a corporate design which includes all forms of marketing materials including business cards, stationery, brochures, case studies, power point standards, product labels and signage.
Corporate standards will include corporate colours matching the corporate logo (Green). Designs will be strong and bold but communicate the environmentally sensitive nature of the products we market.
We have attached corporate logos as well as previous efforts to create a standard for collateral literature and case studies as examples of previous attempts which we are not happy with.
The final designs should be formatted in such a way that Brightfold staff are able to change copy, wording and photos on the body of the brochure without the need of an artist or special effort. If special software is needed to accomplish this, that will need to be specified.
For more information on the company view www.brightfoldresources.ca

Target Market(s)

Oil & Gas Industry, Marine & Aviation & Hospitality Industry

Industry/Entity Type

Chemical Product

Font styles to use
Sans Serif

Colors

Designer to choose colors to be used in the design.

Requirements
Must have
• Include standards for business card, letterhead, 1 page brochure, case studies of 3 - 5 pages, basic standard power point background, product label which can be adjusted for change of product type and volumes in container. Common theme throughout.
Nice to have
• I am open to suggestions. Looking for strong theme which denotes a solid corporation..
• Corporate logo colours are green but is not absolutely essential that the theme be only green. Can incorporate several colours if it compliments the basic logo.
Should not have
• Do not want to have a rainbow of colours or be flashy. Should look like a solid responsible corporation

```html
<!DOCTYPE html>
<html lang="en">
<head>
<meta charset="utf-8">
<title>Brightfold Resources – Stationery Standards</title>
<link href="https://fonts.googleapis.com/css2?family=Montserrat:wght@400;500;600&display=swap" rel="stylesheet">
<style>
  :root{
    --bg:#939598;
    --green:#3a9443;
    --green-dark:#2f7d37;
    --ink:#4a4a4a;
    --paper:#ffffff;
    --photo-sky:#3c4552;
    --photo-sun:#c8641c;
    --photo-ground:#111111;
  }
  *{margin:0;padding:0;box-sizing:border-box}
  html,body{width:1200px;height:870px;overflow:hidden}
  body{background:var(--bg);font-family:"Montserrat",sans-serif;color:var(--ink);position:relative}
  .piece{position:absolute;background:var(--paper);overflow:hidden;box-shadow:0 1px 3px rgba(0,0,0,.18)}
  .piece > svg.shapes{position:absolute;left:0;top:0;width:100%;height:100%}
  .brand{position:absolute;display:flex;flex-direction:column;align-items:center;transform:translateX(-50%)}
  .brand-square{background:var(--green)}
  .brand-name{font-weight:500;color:var(--ink);white-space:nowrap;letter-spacing:-.01em}
  .contact-bar{position:absolute;display:flex;align-items:flex-start}
  .contact-item{display:flex;align-items:center;color:var(--ink);white-space:nowrap;border-left:.6px solid var(--green)}
  .contact-icon{border:.6px solid var(--green);border-radius:1px;display:inline-block}

  /* business cards */
  .card-front{left:74px;top:210px;width:146px;height:83px}
  .card-front .brand{left:73px;top:32px}
  .card-front .brand-square{width:8px;height:8px;margin-bottom:4px}
  .card-front .brand-name{font-size:7px}
  .card-back{left:230px;top:210px;width:145px;height:83px}
  .card-title{position:absolute;left:8px;top:28px;font-size:6px;font-weight:500;color:var(--green)}
  .card-subtitle{position:absolute;left:8px;top:35px;font-size:2.8px;color:var(--ink);letter-spacing:.08em}
  .card-lines{position:absolute;left:8px;top:44px;list-style:none}
  .card-lines li{font-size:3px;line-height:7px;display:flex;align-items:center;gap:3px}
  .card-lines li::before{content:"";width:3px;height:3px;background:var(--green);display:inline-block}
  .card-side-name{position:absolute;left:106px;top:12px;width:16px;height:70px;display:flex;align-items:center;justify-content:center}
  .card-side-name span{transform:rotate(90deg);font-size:4.4px;font-weight:500;white-space:nowrap;color:var(--ink)}

  /* envelope */
  .envelope{left:444px;top:79px;width:374px;height:214px;border-radius:28px 28px 0 0}
  .envelope-url{position:absolute;left:0;top:15px;width:100%;text-align:center;font-size:7px;color:var(--paper);letter-spacing:.12em;transform:rotate(180deg)}
  .envelope .brand{left:104px;top:64px}
  .envelope .brand-square{width:12px;height:12px;margin-bottom:5px}
  .envelope .brand-name{font-size:8px}
  .envelope .contact-bar{left:20px;top:193px}
  .envelope .contact-item{font-size:5px;height:14px;padding:0 6px 0 0;gap:3px;align-items:flex-start}
  .envelope .contact-icon{width:6px;height:6px}

  /* letterhead */
  .letterhead{left:69px;top:315px;width:343px;height:485px}
  .letterhead .brand{left:171px;top:16px}
  .letterhead .brand-square{width:22px;height:22px;margin-bottom:7px}
  .letterhead .brand-name{font-size:12.5px}
  .letterhead .contact-bar{left:14px;top:465px}
  .letterhead .contact-item{font-size:4.8px;height:16px;padding:0 5px 0 0;gap:3px;align-items:flex-start}
  .letterhead .contact-icon{width:6px;height:6px}

  /* presentation folder */
  .folder{left:444px;top:315px;width:687px;height:485px}
  .folder-front-name{position:absolute;left:446px;top:32px;display:flex;align-items:center;gap:10px}
  .folder-front-name .brand-square{width:36px;height:36px}
  .folder-front-name .brand-name{font-size:17px;font-weight:400;line-height:1.05;letter-spacing:.08em;color:var(--ink)}
  .folder-back-name{left:161px;top:368px}
  .folder-back-name .brand-square{width:24px;height:24px;margin-bottom:7px}
  .folder-back-name .brand-name{font-size:12.5px}
  .folder .contact-bar{left:22px;top:462px}
  .folder .contact-item{font-size:5px;height:22px;padding:0 6px 0 0;gap:3px;align-items:flex-start}
  .folder .contact-icon{width:7px;height:7px}
</style>
</head>
<body>

<!-- Business card: front -->
<section class="piece card-front">
  <svg class="shapes" viewBox="0 0 146 83" aria-hidden="true">
    <path d="M0 0H22L15 14Q12 20 6 20H0Z" fill="var(--green)"/>
    <path d="M146 62V83H123L131 67Q134 62 140 62Z" fill="var(--green)"/>
  </svg>
  <div class="brand">
    <span class="brand-square"></span>
    <span class="brand-name">BRIGHTFOLD RESOURCES</span>
  </div>
</section>

<!-- Business card: back -->
<section class="piece card-back">
  <svg class="shapes" viewBox="0 0 145 83" aria-hidden="true">
    <path d="M0 0H22L15 14Q12 20 6 20H0Z" fill="var(--green)"/>
    <path d="M62 83L98 16Q102 8 110 8H145V83Z" fill="var(--green)"/>
    <rect x="104" y="10" width="20" height="73" fill="var(--paper)"/>
  </svg>
  <p class="card-title">TITLE NAME LOREM</p>
  <p class="card-subtitle">LOREM IPSUM</p>
  <ul class="card-lines">
    <li>Main office address line</li>
    <li>+00 0000 0000 00</li>
    <li>+00 0000 0000 00</li>
    <li>info@brightfoldresources.ca</li>
    <li>www.brightfoldresources.ca</li>
  </ul>
  <div class="card-side-name"><span>BRIGHTFOLD RESOURCES</span></div>
</section>

<!-- Envelope -->
<section class="piece envelope">
  <svg class="shapes" viewBox="0 0 374 214" aria-hidden="true">
    <rect x="0" y="0" width="374" height="47" fill="var(--green)"/>
    <path d="M0 47H48L36 80Q31 93 18 93H0Z" fill="var(--green)"/>
    <path d="M374 146V214H292L315 166Q324 146 344 146Z" fill="var(--green)"/>
  </svg>
  <p class="envelope-url">www.brightfoldresources.ca</p>
  <div class="brand">
    <span class="brand-square"></span>
    <span class="brand-name">BRIGHTFOLD RESOURCES</span>
  </div>
  <div class="contact-bar">
    <span class="contact-item"><i class="contact-icon"></i>Lorem ipsum dolor sit amet</span>
    <span class="contact-item"><i class="contact-icon"></i>+00 0000 0000 00</span>
    <span class="contact-item"><i class="contact-icon"></i>info@bfr.com</span>
    <span class="contact-item"><i class="contact-icon"></i>www.bfr.com</span>
  </div>
</section>

<!-- Letterhead -->
<section class="piece letterhead">
  <svg class="shapes" viewBox="0 0 343 485" aria-hidden="true">
    <path d="M0 0H48L34 32Q28 45 14 45H0Z" fill="var(--green)"/>
    <path d="M343 402V485H262L289 422Q298 402 320 402Z" fill="var(--green)"/>
  </svg>
  <div class="brand">
    <span class="brand-square"></span>
    <span class="brand-name">BRIGHTFOLD RESOURCES</span>
  </div>
  <div class="contact-bar">
    <span class="contact-item"><i class="contact-icon"></i>Lorem ipsum dolor sit amet</span>
    <span class="contact-item"><i class="contact-icon"></i>+00 0000 0000 00</span>
    <span class="contact-item"><i class="contact-icon"></i>info@bfr.com</span>
    <span class="contact-item"><i class="contact-icon"></i>www.bfr.com</span>
  </div>
</section>

<!-- Presentation folder -->
<section class="piece folder">
  <svg class="shapes" viewBox="0 0 687 485">
    <defs>
      <linearGradient id="sunsetFill" x1="0" y1="0" x2="0" y2="1">
        <stop offset="0" stop-color="var(--photo-sky)"/>
        <stop offset=".45" stop-color="#6a4a3a"/>
        <stop offset=".62" stop-color="var(--photo-sun)"/>
        <stop offset=".78" stop-color="var(--photo-ground)"/>
        <stop offset="1" stop-color="var(--photo-ground)"/>
      </linearGradient>
      <linearGradient id="panelGreen" x1="0" y1="0" x2="1" y2="1">
        <stop offset="0" stop-color="var(--green)"/>
        <stop offset="1" stop-color="var(--green-dark)"/>
      </linearGradient>
    </defs>
    <path role="img" aria-label="Photo: oil pump jack silhouetted against a sunset sky"
          d="M0 0H312L238 178Q190 320 64 325H0Z" fill="url(#sunsetFill)"/>
    <path d="M0 0H148L112 82Q92 137 30 137H0Z" fill="var(--green)"/>
    <path d="M300 485L440 168Q472 93 566 93H687V485Z" fill="url(#panelGreen)"/>
    <path role="img" aria-label="Photo: oil pump jack silhouetted against a sunset sky"
          d="M384 429L500 198Q526 145 586 145H687V429Z" fill="url(#sunsetFill)"
          stroke="var(--paper)" stroke-width="3"/>
  </svg>
  <div class="folder-front-name">
    <span class="brand-square"></span>
    <span class="brand-name">BRIGHTFOLD<br>RESOURCES</span>
  </div>
  <div class="brand folder-back-name">
    <span class="brand-square"></span>
    <span class="brand-name">BRIGHTFOLD RESOURCES</span>
  </div>
  <div class="contact-bar">
    <span class="contact-item"><i class="contact-icon"></i>Lorem ipsum dolor sit amet</span>
    <span class="contact-item"><i class="contact-icon"></i>+00 0000 0000 00</span>
    <span class="contact-item"><i class="contact-icon"></i>info@bfr.com</span>
    <span class="contact-item"><i class="contact-icon"></i>www.bfr.com</span>
  </div>
</section>

</body>
</html>
```